Business Card Design for RT Wine:

I'm looking for a card that has the following.
Front:
- Merlot Colored
- stripe down the middle in silver or gold flake
- RT in block like thick letters with gold or silver flake above stripe
-Wine: below stripe
- a grape bunch that is at the end of the stripe that is made so it can be printed as embossed
Back:
- line down the middle of card in Merlot, card is white background
- to the left Marisa Dobbs, (next line) Owner, (next line) Certified Sommelier, BPL
- to the right (listed) restaurant consulting, wine tours, personal tastings, event planning, personal wine buying
- add embossed grape bunch
Also, looking for a piece that slides over like a envelope for a room key for a hotel that says "We met @ VANDORA" and possibly a file for that, that I can edit.
Would like card to be printed on a thicker cardstock

```html
<!DOCTYPE html>
<html lang="en">
<head>
<meta charset="utf-8">
<title>RT Wine — Business Card</title>
<link rel="stylesheet" href="https://fonts.googleapis.com/css2?family=Arimo:wght@400;700&family=Oswald:wght@700&display=swap">
<style>
  :root {
    --bg: #e6e6e6;
    --merlot-light: #5e2e37;
    --merlot-dark: #3e161c;
    --gold: #b8913a;
    --silver-light: #f2f2f2;
    --silver-mid: #c9c9c9;
    --silver-dark: #8e8e8e;
    --ink: #111111;
    --paper: #ffffff;
    --divider: #4a1d24;
  }
  * { box-sizing: border-box; margin: 0; padding: 0; }
  html, body { width: 1200px; height: 1000px; overflow: hidden; }
  body {
    background: var(--bg);
    font-family: "Arimo", Arial, sans-serif;
    position: relative;
  }
  .card {
    position: absolute;
    left: 280px;
    width: 640px;
    height: 366px;
    overflow: hidden;
    box-shadow: 0 2px 8px rgba(0,0,0,0.15);
  }

  /* Back */
  .card-back { top: 100px; background: var(--paper); color: var(--ink); }
  .card-back .divider {
    position: absolute; left: 300px; top: 30px; width: 3px; height: 306px;
    background: var(--divider);
  }
  .card-back .identity { position: absolute; left: 30px; top: 40px; width: 260px; }
  .card-back .name {
    font-family: "Oswald", Impact, sans-serif; font-weight: 700;
    font-size: 34px; letter-spacing: 1px; line-height: 1.1; text-transform: uppercase;
  }
  .card-back .role { font-size: 28px; line-height: 1.2; }
  .card-back .credential { font-size: 21px; line-height: 1.3; margin-top: 14px; }
  .card-back .services {
    position: absolute; left: 326px; top: 64px; list-style: none;
    font-size: 22px; line-height: 1.25;
  }

  /* Front */
  .card-front {
    top: 530px;
    background: linear-gradient(90deg, var(--merlot-light), var(--merlot-dark));
  }
  .card-front .monogram {
    position: absolute; left: 0; width: 600px; top: 52px; text-align: center;
    font-family: "Arimo", Arial, sans-serif; font-weight: 700;
    font-size: 92px; line-height: 1; color: var(--gold); letter-spacing: 2px;
  }
  .card-front .stripe {
    position: absolute; left: 0; right: 0; top: 160px; height: 38px;
    background: linear-gradient(90deg, var(--silver-mid) 0%, var(--silver-light) 40%, var(--silver-mid) 70%, var(--silver-dark) 100%);
  }
  .card-front .tagline {
    position: absolute; left: 27px; top: 220px;
    font-size: 28px; color: var(--paper); letter-spacing: 0.5px;
  }
  .card-front .grape-bunch {
    position: absolute; left: 512px; top: 84px; width: 118px; height: 104px;
  }
</style>
</head>
<body>
  <section class="card card-back" aria-label="Card back">
    <div class="identity">
      <h1 class="name">Marisa Dobbs</h1>
      <p class="role">Owner</p>
      <p class="credential">Certified Sommelier, BPL</p>
    </div>
    <div class="divider"></div>
    <ul class="services">
      <li>Restaurant Consulting,</li>
      <li>Wine Tours,</li>
      <li>Personal Tastings,</li>
      <li>Event Planning,</li>
      <li>Personal Wine Buying</li>
    </ul>
  </section>

  <section class="card card-front" aria-label="Card front">
    <div class="monogram">RT</div>
    <div class="stripe"></div>
    <svg class="grape-bunch" viewBox="0 0 118 104" role="img" aria-label="Embossed grape bunch illustration">
      <ellipse cx="52" cy="54" rx="42" ry="46" fill="#d8d4d5" opacity="0.55"/>
    </svg>
    <p class="tagline">WINE</p>
  </section>
</body>
</html>
```